Talent Management Company Needs Business Cards

Using one of the logos provided (attached) K&R Talent Collective needs a business card designed.
Please visit our website for more information about us-

www.krtalentcollective.example

The face should feature a dramatic presentation of the logo with the back being reserved for our professional information which is:

The information should be:
Dorian T. Vickers
C.E.O
Email: dtvickers@krtalentcollective.example
Mobile: 555-804-2917
Website: www.krtalentcollective.example

Marcus L. Vickers
Director of Public Relations
Email: mlvickers@krtalentcollective.example
Mobile: 555-806-3350

Jules R. Hampton
Director of Client Development
Email: jhampton@krtalentcollective.example

Simon Hurlock
Director of Brand Development
Email: shurlock@krtalentcollective.example

Would like the logo to have color. I would like to see one side red or black and the other side white but if it looks better in either black or red that would be fine to but would like to see how it comes out.

Please feel free to message me and if you would like just the icon alone I have other image files that I can send as well.

Target Market(s)

Professional Athletes, coaches, entertainers age 18-35 but also must be accepted in the business community

Industry/Entity Type

Business

Requirements
Must have
• 1) Use the logo
2) Double sided
3) Distinctive
Nice to have
• Small simple images for telephone, e-mail, and Url.

```html
<!DOCTYPE html>
<html lang="en">
<head>
<meta charset="utf-8">
<title>K&amp;R Talent Collective — Business Card</title>
<link href="https://fonts.googleapis.com/css2?family=Lato:wght@400;700&display=swap" rel="stylesheet">
<style>
  :root {
    --bg: #e9e6e1;
    --card-white: #f4f4f4;
    --ink: #2a2a2a;
    --ink-soft: #3c3c3c;
    --red: #c8161c;
    --red-deep: #7a0b0e;
    --red-dark: #4a0607;
    --white: #ffffff;
    --rule-light: rgba(255,255,255,0.55);
  }
  * { box-sizing: border-box; margin: 0; padding: 0; }
  html, body {
    width: 1200px; height: 720px; overflow: hidden;
    background: var(--bg);
    font-family: "Lato", Arial, sans-serif;
  }
  .canvas {
    position: relative; width: 1200px; height: 720px;
    display: flex; align-items: center; justify-content: center; gap: 60px;
  }
  .card {
    width: 520px; height: 298px; position: relative;
    box-shadow: 0 6px 18px rgba(0,0,0,0.18);
  }

  /* Back: contact side */
  .card--back {
    background: var(--card-white);
    color: var(--ink);
    text-align: center;
  }
  .brand {
    display: flex; align-items: center; justify-content: center; gap: 10px;
    font-weight: 700; letter-spacing: 0.5px;
  }
  .brand__dot {
    width: 14px; height: 14px; border-radius: 50%;
    background: var(--red); flex: none;
  }
  .card--back .brand { margin-top: 40px; font-size: 19px; color: var(--ink); }
  .person__name { margin-top: 34px; font-size: 26px; font-weight: 400; color: var(--ink); }
  .person__title { margin-top: 2px; font-size: 15px; color: var(--ink-soft); letter-spacing: 0.5px; }
  .rule--red {
    margin: 14px auto 0; width: 440px; height: 1px;
    background: linear-gradient(90deg, transparent, var(--red) 30%, var(--red) 70%, transparent);
  }
  .contact { margin-top: 12px; font-size: 13.5px; color: var(--ink); line-height: 1.7; }
  .contact__row { display: flex; justify-content: center; align-items: center; gap: 18px; }
  .contact__item { display: inline-flex; align-items: center; gap: 6px; }
  .icon { width: 13px; height: 13px; fill: none; stroke: var(--red); stroke-width: 1.6; }
  .icon--solid { fill: var(--red); stroke: none; }

  /* Face: logo side */
  .card--face {
    background: radial-gradient(ellipse at 20% 15%, var(--red) 0%, #a80f14 45%, var(--red-deep) 80%, var(--red-dark) 100%);
    color: var(--white);
    text-align: center;
  }
  .card--face .brand { padding-top: 110px; font-size: 27px; color: var(--white); }
  .card--face .brand__dot { width: 20px; height: 20px; background: var(--white); }
  .rule--light {
    margin: 20px auto 0; width: 400px; height: 1px;
    background: linear-gradient(90deg, transparent, var(--rule-light) 35%, var(--rule-light) 65%, transparent);
  }
  .face__web { margin-top: 10px; font-size: 13px; letter-spacing: 0.4px; color: var(--white); }
</style>
</head>
<body>
<main class="canvas">
  <section class="card card--back" aria-label="Card back with contact details">
    <div class="brand"><span class="brand__dot"></span><span class="brand__name">K&amp;R Talent Collective</span></div>
    <h1 class="person__name">Dorian T. Vickers</h1>
    <p class="person__title">C.E.O</p>
    <div class="rule--red"></div>
    <div class="contact">
      <div class="contact__row">
        <span class="contact__item">
          <svg class="icon" viewBox="0 0 14 14" aria-hidden="true"><rect x="1" y="3" width="12" height="8"/><path d="M1 3l6 5 6-5"/></svg>
          dtvickers@krtalentcollective.example
        </span>
        <span class="contact__item">
          <svg class="icon" viewBox="0 0 14 14" aria-hidden="true"><rect x="4" y="1" width="6" height="12" rx="1"/><path d="M4 10h6"/></svg>
          555-804-2917
        </span>
      </div>
      <div class="contact__row">
        <span class="contact__item">
          <svg class="icon icon--solid" viewBox="0 0 14 14" aria-hidden="true"><path d="M7 1L1 7h2v6h3V9h2v4h3V7h2z"/></svg>
          www.krtalentcollective.example
        </span>
      </div>
    </div>
  </section>

  <section class="card card--face" aria-label="Card face with company name">
    <div class="brand"><span class="brand__dot"></span><span class="brand__name">K&amp;R Talent Collective</span></div>
    <div class="rule--light"></div>
    <p class="face__web">www.krtalentcollective.example</p>
  </section>
</main>
</body>
</html>
```